Namecard Designs+Logo for a High End Automobile Company

We need a new business card for our company called Velta Motorhof.

www.veltamotorhof.example.sg
Our new website will be up in 2.5 months time.

We sell used and brand new continental cars like Korvane, QTL, Dravell, Solbrini and etc. Currently we are operating from 2 offices in Singapore and United Kingdom.

We want a design which is serious. We are open to colours but try to keep it at a maximum of 3 colours.

We prefer something simple and minimal. We are open to 2 sides printing or even 2 sided namecards. Both UK and Singapore company offices address must be in; either side by side, front and back, or even 2 sided cards.

The logo can be a text logo, emblem, abstract, pictorial or combination.

We are printing with Pribo.com so please kindly follow the printing guideline.

http://uk.pribo.example/help/faq/templates-and-guidelines.html

Rich and Car Enthusiasts

Printing

Must have
• Our 2 offices; UK and Singapore.

Our slogan which is " The Automobile Specialist"
Should not have
• Not more than 3 colours

```html
<!DOCTYPE html>
<html lang="en">
<head>
<meta charset="utf-8">
<title>Velta Motorhof – Business Card</title>
<link rel="stylesheet" href="https://fonts.googleapis.com/css2?family=Archivo+Black&family=M+PLUS+1p:wght@400;500&display=swap">
<style>
  :root {
    --card: #ffffff;
    --ink: #111111;
    --brand: #2b2424;
    --map: #dedede;
    --car: #d4d4d4;
  }
  html, body {
    margin: 0;
    padding: 0;
    width: 1200px;
    height: 806px;
    overflow: hidden;
    background: var(--card);
  }
  .card {
    position: relative;
    width: 1200px;
    height: 806px;
    background: var(--card);
    color: var(--ink);
    font-family: "M PLUS 1p", "Helvetica Neue", Arial, sans-serif;
    overflow: hidden;
  }
  .world-map {
    position: absolute;
    left: 294px;
    top: 46px;
    width: 664px;
    height: 727px;
    border-radius: 46% 42% 40% 48%;
    background: radial-gradient(ellipse at 50% 45%, var(--map) 0%, rgba(222,222,222,0.55) 55%, rgba(255,255,255,0) 78%);
  }
  .car-illustration {
    position: absolute;
    left: 865px;
    top: 87px;
    width: 266px;
    height: 155px;
    border-radius: 40% 50% 18% 18%;
    background: linear-gradient(180deg, rgba(212,212,212,0.25) 0%, rgba(212,212,212,0.6) 100%);
  }
  .brand-name {
    position: absolute;
    left: 115px;
    top: 92px;
    margin: 0;
    font-family: "Archivo Black", "Arial Black", sans-serif;
    font-size: 62px;
    line-height: 1;
    letter-spacing: 2px;
    color: var(--brand);
    font-weight: 400;
  }
  .slogan {
    position: absolute;
    left: 102px;
    top: 170px;
    margin: 0;
    font-family: "Archivo Black", "Arial Black", sans-serif;
    font-size: 37px;
    line-height: 1;
    letter-spacing: 3px;
    color: var(--brand);
  }
  .person {
    position: absolute;
    left: 0;
    width: 1208px;
    text-align: center;
    margin: 0;
    font-weight: 400;
  }
  .person-name { top: 292px; font-size: 54px; line-height: 1; }
  .person-title { top: 366px; font-size: 38px; line-height: 1; }
  .office {
    position: absolute;
    margin: 0;
    font-style: normal;
    text-align: center;
    font-size: 23px;
    line-height: 34.7px;
  }
  .office-heading { text-decoration: underline; text-underline-offset: 3px; }
  .office-uk { left: 69px; width: 400px; top: 483px; }
  .office-sg { left: 712px; width: 400px; top: 474px; }
  .website {
    position: absolute;
    left: 0;
    width: 1208px;
    top: 688px;
    text-align: center;
    font-size: 30px;
    line-height: 1;
    text-decoration: underline;
    text-underline-offset: 4px;
    color: var(--ink);
  }
</style>
</head>
<body>
  <main class="card">
    <div class="world-map" role="img" aria-label="Faint grey world map showing the Americas"></div>
    <div class="car-illustration" role="img" aria-label="Line drawing of a sports car"></div>

    <h1 class="brand-name">Velta Motorhof</h1>
    <p class="slogan">“The Automobile Specialist”</p>

    <h2 class="person person-name">Marlo Venn</h2>
    <p class="person person-title">Sales maneger</p>

    <address class="office office-uk">
      <span class="office-heading">UK office</span><br>
      48 Ashgrove st.<br>
      London 00000<br>
      Tel 020 0000 4417<br>
      Email info@veltamotorhof.example
    </address>

    <address class="office office-sg">
      <span class="office-heading">Singapore office</span><br>
      Harlow rd. one harlow<br>
      #02-01 singapore 000000<br>
      Tel +65 0000 7723<br>
      Email sg@veltamotorhof.example
    </address>

    <p class="website">http://veltamotorhof.example.sg</p>
  </main>
</body>
</html>
```